Business Card for Business consulting practice

Need a design for a consultant business card. Simple and elegant.
I need the following information on the card:
Logo: (see uploaded file)
Company name: Callendry Advisory Group
Name: Noel Fardwick
Title: Managing Director - Aerospace and Defence
Phone #: 438-261-7083
e-mail: noel.fardwick@callendry.example
Website: www.callendry.example
Tagline: Proposals Management and Capture support for complex procurements

```html
<!DOCTYPE html>
<html lang="en">
<head>
<meta charset="utf-8">
<title>Callendry Advisory Group — Business Card</title>
<link href="https://fonts.googleapis.com/css2?family=Montserrat:wght@400;500;600&display=swap" rel="stylesheet">
<style>
  :root {
    --navy: #213849;
    --blue: #1793c0;
    --white: #ffffff;
    --backdrop: #f4f4f4;
  }
  html, body {
    margin: 0;
    padding: 0;
    width: 1200px;
    height: 1200px;
    overflow: hidden;
    background: var(--backdrop);
    font-family: "Montserrat", Arial, sans-serif;
  }
  .card {
    position: absolute;
    left: 225px;
    width: 754px;
    height: 430px;
    overflow: hidden;
  }
  .card--front { top: 138px; background: var(--white); }
  .card--back { top: 635px; background: var(--navy); }

  .brand {
    position: absolute;
    right: 44px;
    top: 44px;
    text-align: right;
  }
  .brand__name {
    margin: 0;
    font-weight: 600;
    font-size: 22px;
    letter-spacing: 1.5px;
    color: var(--navy);
    line-height: 1;
    text-transform: uppercase;
  }
  .brand__tagline {
    margin: 26px 0 0;
    font-weight: 600;
    font-size: 7px;
    letter-spacing: 0.3px;
    color: var(--blue);
    text-transform: uppercase;
  }

  .person {
    position: absolute;
    left: 40px;
    top: 186px;
    width: 674px;
    border-bottom: 1.5px solid var(--blue);
    padding-bottom: 7px;
  }
  .person__name {
    margin: 0;
    font-weight: 500;
    font-size: 29px;
    line-height: 1;
    letter-spacing: 0.5px;
    color: var(--navy);
    text-transform: uppercase;
  }
  .person__surname { color: var(--blue); }
  .person__title {
    margin: 6px 0 0;
    font-weight: 600;
    font-size: 8px;
    letter-spacing: 0.4px;
    color: var(--navy);
    text-transform: uppercase;
  }

  .contacts {
    position: absolute;
    left: 39px;
    top: 255px;
    margin: 0;
    padding: 0;
    list-style: none;
  }
  .contacts__item {
    display: flex;
    align-items: center;
    height: 31.5px;
    font-size: 20px;
    font-weight: 500;
    color: var(--navy);
  }
  .contacts__icon {
    width: 26px;
    height: 26px;
    margin-right: 14px;
    flex: none;
  }

  .footer-band {
    position: absolute;
    left: 0;
    right: 0;
    top: 375px;
    height: 43px;
    background: linear-gradient(to right, var(--blue) 0 556px, var(--navy) 556px 100%);
  }
  .footer-band__mark {
    position: absolute;
    left: 524px;
    top: -11px;
    width: 64px;
    height: 64px;
  }

  .back-brand {
    position: absolute;
    left: 0;
    right: 0;
    top: 150px;
    text-align: center;
  }
  .back-brand__name {
    margin: 0;
    font-weight: 600;
    font-size: 40px;
    letter-spacing: 3px;
    line-height: 1;
    color: var(--white);
    text-transform: uppercase;
  }
  .back-brand__tagline {
    margin: 58px 0 0;
    font-weight: 500;
    font-size: 11px;
    letter-spacing: 0.4px;
    color: var(--blue);
    text-transform: uppercase;
  }
</style>
</head>
<body>

<section class="card card--front">
  <header class="brand">
    <p class="brand__name">Callendry Advisory Group</p>
    <p class="brand__tagline">Proposals Management and Capture Support for Complex Procurements</p>
  </header>

  <div class="person">
    <h1 class="person__name">Noel <span class="person__surname">Fardwick</span></h1>
    <p class="person__title">Managing Director - Aerospace and Defence</p>
  </div>

  <ul class="contacts">
    <li class="contacts__item">
      <svg class="contacts__icon" viewBox="0 0 26 26" aria-hidden="true">
        <circle cx="13" cy="13" r="13" fill="var(--blue)"/>
        <path d="M9.2 6.5c.6-.3 1.2-.1 1.5.4l1.4 2.4c.3.5.2 1.1-.3 1.5l-1 .8c.7 1.6 2 3 3.6 3.7l.8-1c.4-.5 1-.6 1.5-.3l2.4 1.4c.5.3.7 1 .4 1.5l-.8 1.3c-.5.8-1.5 1.1-2.4.8-3.6-1.3-6.4-4.1-7.7-7.7-.3-.9 0-1.9.8-2.4z" fill="var(--white)"/>
      </svg>
      438-261-7083
    </li>
    <li class="contacts__item">
      <svg class="contacts__icon" viewBox="0 0 26 26" aria-hidden="true">
        <circle cx="13" cy="13" r="13" fill="var(--blue)"/>
        <rect x="6.5" y="8.5" width="13" height="9" fill="none" stroke="var(--white)" stroke-width="1.3"/>
        <path d="M6.5 8.5l6.5 5.2 6.5-5.2M6.5 17.5l4.6-4.4M19.5 17.5l-4.6-4.4" fill="none" stroke="var(--white)" stroke-width="1.1"/>
      </svg>
      noel.fardwick@callendry.example
    </li>
    <li class="contacts__item">
      <svg class="contacts__icon" viewBox="0 0 26 26" aria-hidden="true">
        <circle cx="13" cy="13" r="13" fill="var(--blue)"/>
        <circle cx="13" cy="13" r="7.5" fill="none" stroke="var(--white)" stroke-width="1.3"/>
        <path d="M5.5 13h15M13 5.5c-3 3.5-3 11.5 0 15M13 5.5c3 3.5 3 11.5 0 15" fill="none" stroke="var(--white)" stroke-width="1"/>
      </svg>
      www.callendry.example
    </li>
  </ul>

  <div class="footer-band">
    <svg class="footer-band__mark" viewBox="0 0 64 64" aria-hidden="true">
      <circle cx="32" cy="32" r="30" fill="var(--white)"/>
      <circle cx="32" cy="32" r="24" fill="none" stroke="var(--blue)" stroke-width="4"/>
    </svg>
  </div>
</section>

<section class="card card--back">
  <div class="back-brand">
    <p class="back-brand__name">Callendry Advisory Group</p>
    <p class="back-brand__tagline">Proposals Management and Capture Support for Complex Procurements</p>
  </div>
</section>

</body>
</html>
```